A Real Estate Company Needs a Business Card Design

We need a business card design for a new company based in Boston MA called "Brackenfield Real Estate LLC" we are a small company but we like a big corporate look, a simple, sleek, modern and progressive look. we would like the option of having a design that could include the real estate agents personal photo and also a design if the realtor decides not to have a photo. we do not have LOGO at this moment, please use any property look pic corporate with word" Brackenfield Real Estate LLC" please see attached file as an example.
Industry/Entity Type
Business

```html
<!DOCTYPE html>
<html lang="en">
<head>
<meta charset="utf-8">
<title>Brackenfield Real Estate LLC – Business Card</title>
<link rel="stylesheet" href="https://fonts.googleapis.com/css2?family=Arimo:wght@400;700&display=swap">
<style>
  :root {
    --backdrop: #7b4535;
    --card: #ffffff;
    --brand: #7a1505;
    --ink: #2b2b2b;
    --ink-soft: #3a3a3a;
  }
  * { margin: 0; padding: 0; box-sizing: border-box; }
  html, body { width: 1200px; height: 900px; overflow: hidden; }
  body {
    background: var(--backdrop);
    font-family: "Arimo", Arial, sans-serif;
    position: relative;
  }
  .card {
    position: absolute;
    width: 444px;
    height: 255px;
    background: var(--card);
    border-radius: 30px 30px 0 0;
    overflow: hidden;
  }
  /* Front */
  .card-front { left: 228px; top: 192px; }
  .brand-square {
    position: absolute;
    left: 200px; top: 34px;
    width: 44px; height: 44px;
    background: var(--brand);
  }
  .brand-name {
    position: absolute;
    left: 0; right: 0; top: 132px;
    text-align: center;
    color: var(--brand);
    font-weight: 400;
    font-size: 30px;
    letter-spacing: 1px;
    line-height: 1;
  }
  .brand-tagline {
    position: absolute;
    left: 84px; right: 84px; top: 166px;
    display: flex; align-items: center; gap: 6px;
    color: var(--brand);
    font-weight: 400;
    font-size: 13px;
    letter-spacing: 2px;
    line-height: 1;
  }
  .brand-tagline::before,
  .brand-tagline::after {
    content: ""; flex: 1; height: 1.5px; background: var(--brand);
  }
  .front-rule {
    position: absolute; left: 0; right: 0; top: 220px;
    height: 2px; background: var(--brand);
  }
  .front-band {
    position: absolute; left: 0; right: 0; top: 226px; bottom: 0;
    background: var(--brand);
  }
  /* Back */
  .card-back { left: 529px; top: 452px; }
  .info-block {
    position: absolute;
    left: 25px;
    padding-left: 13px;
    border-left: 2px solid var(--brand);
    color: var(--ink);
  }
  .agent { top: 38px; }
  .agent-name { font-size: 12px; line-height: 14px; color: var(--ink-soft); }
  .agent-line { font-size: 9.5px; line-height: 13px; }
  .office { top: 168px; }
  .office-name { font-size: 16px; line-height: 20px; color: var(--ink-soft); margin-bottom: 3px; }
  .office-line { font-size: 9.5px; line-height: 12.5px; }
  .back-mark {
    position: absolute;
    right: 50px; top: 38px;
    display: flex; flex-direction: column; align-items: center; gap: 6px;
  }
  .back-square { width: 40px; height: 40px; background: var(--brand); }
  .back-name {
    color: var(--brand);
    font-weight: 400;
    font-size: 9px;
    letter-spacing: 1px;
  }
</style>
</head>
<body>
  <section class="card card-front" aria-label="Business card front">
    <div class="brand-square"></div>
    <div class="brand-name">BRACKENFIELD</div>
    <div class="brand-tagline">REAL ESTATE LLC</div>
    <div class="front-rule"></div>
    <div class="front-band"></div>
  </section>

  <section class="card card-back" aria-label="Business card back">
    <div class="info-block agent">
      <p class="agent-name">DANA K WHITFIELD</p>
      <p class="agent-line">Managing Director</p>
      <p class="agent-line">C&nbsp;:&nbsp; + 03 5550 2741</p>
    </div>

    <div class="back-mark">
      <div class="back-square"></div>
      <div class="back-name">BRACKENFIELD</div>
    </div>

    <div class="info-block office">
      <p class="office-name">Brackenfield Real Estate LLC</p>
      <p class="office-line">PO Box 418, Harbourview VIC 3120</p>
      <p class="office-line">T&nbsp;:&nbsp; + 03 5550 2741</p>
      <p class="office-line">F&nbsp;:&nbsp; + 03 5550 2796</p>
      <p class="office-line">E&nbsp;:&nbsp; info@brackenfieldrealestate.com</p>
    </div>
  </section>
</body>
</html>
```